Flyer Design

Create a flyer using the logo theme. Single page for to be sent out on email. Attached is an image of the layout, below is the text. A5 and a4 versions.

Simplifying the MAZE

This short workshop is designed as a refresher for those surgeons who have attended a full Lund-MAZE training course, and wish to gain an update on the latest thinking with regards to the surgical treatment of Atrial Fibrillation.
We will start with an overview of the disease burden, talk to the foundation clinical evidence available, and cover the various lesion sets used by surgeons – with a view to simplifying the procedure. The workshop will also explain the technology used, how to treat the Left Atrial Appendage, the best ways to work with your EP colleagues, and involve a short hands-on session to familiarize you with the tools available to perform the Lund-MAZE procedure.

Faculty
{{image}}
Mr. Declan Harlow
Cardiothoracic Surgeon

Mr Harlows training was completed at the Brenhill Clinic, Rochester, Minnesota, between June 1995 and July 1997 followed by an advanced fellowship with Professor Ferris K Lomond at the Ashgrove General Hospital. Additional expertise required visits to Belgium, Italy, England and the United States. Mr Harlow now proctors internationally in order to share his knowledge and further improvement in all areas of minimal access and open cardiac and thoracic surgery.
Further overseas experience at the Ashgrove General Hospital in Canada culminated in the award of Clinical Fellowship in Cardiovascular Surgery in December 1997.

Mr Harlow has contributed to many publications and is referee for Journal articles in very highly regarded professional journals. He performs both Cardiac surgery procedures and thoracic procedures at Westmere Private Hospital and Dunmore Hospital, Melbourne. Mr Harlow has performed in excess of 200 open Maze procedures and 35 via a Thoracoscopic approach.

Venue - TBA
Time : 5pm - 7.30pm, followed by dinner and case presentations

```html
<!DOCTYPE html>
<html lang="en">
<head>
<meta charset="utf-8">
<title>Simplifying the MAZE – Workshop Flyer</title>
<link href="https://fonts.googleapis.com/css2?family=Lato:wght@400;700;900&display=swap" rel="stylesheet">
<style>
  :root{
    --navy:#0b2a4a;
    --blue:#0a78b8;
    --pale:#cde8f8;
    --orange:#f07f0a;
    --white:#ffffff;
  }
  *{margin:0;padding:0;box-sizing:border-box}
  html,body{width:1000px;height:1200px;overflow:hidden;background:var(--white)}
  .flyer{position:relative;width:1000px;height:1200px;overflow:hidden;font-family:'Lato',sans-serif}
  .flyer-shapes{position:absolute;inset:0}
  .brand{position:absolute;left:648px;top:28px;font-size:62px;font-weight:700;color:var(--white);letter-spacing:-0.5px}
  .speaker-name{position:absolute;left:500px;width:460px;top:446px;text-align:center;font-size:36px;font-weight:700;color:var(--white)}
  .speaker-rule{position:absolute;left:660px;top:494px;width:142px;height:3px;background:var(--white)}
  .speaker-role{position:absolute;left:490px;width:480px;top:504px;text-align:center;font-size:37px;font-weight:700;color:var(--orange)}
  .bio-marker{position:absolute;left:500px;top:552px;width:3px;height:48px;background:var(--navy)}
  .speaker-bio{position:absolute;left:522px;top:550px;width:438px;font-size:18.6px;line-height:20.7px;color:var(--white)}
  .speaker-bio p+p{margin-top:20.7px}
  .workshop-title{position:absolute;left:44px;top:545px;font-size:33px;font-weight:700;color:var(--navy)}
  .title-rule{position:absolute;left:44px;top:596px;width:52px;height:3px;background:var(--navy)}
  .workshop-intro{position:absolute;left:44px;top:609px;width:350px;font-size:18.6px;line-height:20.7px;color:var(--navy)}
  .footer-venue{position:absolute;left:0;top:1106px;width:490px;height:60px;display:flex;align-items:center;justify-content:center;font-size:39px;font-weight:700;color:var(--white)}
  .footer-venue .label{color:var(--orange)}
  .footer-time{position:absolute;left:520px;top:1106px;width:430px;height:60px;text-align:center;color:var(--navy)}
  .footer-time .time-line{font-size:35px;font-weight:700;line-height:38px;margin-top:2px}
  .footer-time .time-value{color:var(--white)}
  .footer-time .time-note{font-size:13px;font-weight:700;line-height:14px}
</style>
</head>
<body>
<div class="flyer">
  <svg class="flyer-shapes" width="1000" height="1200" viewBox="0 0 1000 1200">
    <defs>
      <linearGradient id="surgeryTones" x1="0" y1="0" x2="1" y2="1">
        <stop offset="0" stop-color="#9fd0f0"/>
        <stop offset="0.5" stop-color="#4b9ad8"/>
        <stop offset="1" stop-color="#1f5fa8"/>
      </linearGradient>
      <linearGradient id="portraitTones" x1="0" y1="0" x2="0" y2="1">
        <stop offset="0" stop-color="#123a62"/>
        <stop offset="1" stop-color="#0a2240"/>
      </linearGradient>
    </defs>
    <rect class="pale-field" width="1000" height="1200" fill="var(--pale)"/>
    <path class="navy-band" d="M0 0 H700 V430 L470 428 Q250 470 0 500 Z" fill="var(--navy)"/>
    <g role="img" aria-label="Photograph of surgeons operating in a blue-lit theatre">
      <path d="M0 0 H700 V400 L480 415 Q250 440 0 445 Z" fill="url(#surgeryTones)"/>
    </g>
    <path class="navy-curve" d="M650 0 C534 200 428 450 428 700 C428 900 458 1100 478 1200 H1000 V0 Z" fill="var(--navy)"/>
    <path class="blue-panel" d="M678 0 C560 200 455 450 455 700 C455 900 485 1100 507 1200 H1000 V0 Z" fill="var(--blue)"/>
    <circle class="portrait-ring" cx="730" cy="301" r="160" fill="var(--white)"/>
    <g role="img" aria-label="Portrait of the presenting surgeon">
      <circle cx="730" cy="301" r="148" fill="url(#portraitTones)"/>
    </g>
    <rect class="footer-bar" x="0" y="1106" width="1000" height="60" fill="var(--navy)"/>
    <polygon class="footer-time-band" points="495,1106 1000,1106 1000,1166 518,1166" fill="var(--orange)"/>
  </svg>

  <div class="brand">Cardivel</div>

  <div class="speaker-name">Mr. Declan Harlow</div>
  <div class="speaker-rule"></div>
  <div class="speaker-role">Cardiothoracic Surgeon</div>

  <div class="bio-marker"></div>
  <div class="speaker-bio">
    <p>Mr Harlows Training Was Completed At The Brenhill Clinic, Rochester, Minnesota, Between June 1995 And July 1997 Followed By An Advanced Fellowship With Professor Ferris K Lomond At The Ashgrove General Hospital. Additional Expertise Required Visits To Belgium, Italy, England And The United States. Mr Harlow Now Proctors Internationally In Order To Share His Knowledge And Further Improvement In All Areas Of Minimal Access And Open Cardiac And Thoracic Surgery.</p>
    <p>Further Overseas Experience At The Ashgrove General Hospital In Canada Culminated In The Award Of Clinical Fellowship In Cardiovascular Surgery In December 1997.</p>
    <p>Mr Harlow Has Contributed To Many Publications And Is Referee For Journal Articles In Very Highly Regarded Professional Journals. He Performs Both Cardiac Surgery Procedures And Thoracic Procedures At Westmere Private Hospital And Dunmore Hospital, Melbourne. Mr Harlow Has Performed In Excess Of <b>200</b> Open Maze Procedures And <b>35</b> Via A Thoracoscopic Approach.</p>
  </div>

  <h1 class="workshop-title">Simplifying the MAZE</h1>
  <div class="title-rule"></div>
  <p class="workshop-intro">This short workshop is designed as a refresher for those surgeons who have attended a full Lund-<b>MAZE</b> training course, and wish to gain an update on the latest thinking with regards to the surgical treatment of Atrial Fibrillation. We will start with an overview of the disease burden, talk to the foundation clinical evidence available, and cover the various lesion sets used by surgeons – with a view to simplifying the procedure. The workshop will also explain the technology used, how to treat the Left Atrial Appendage, the best ways to work with your EP colleagues, and involve a short hands-on session to familiarize you with the tools available to perform the Lund-<b>MAZE</b> procedure.</p>

  <div class="footer-venue"><span class="label">VENUE :&nbsp;</span><span>TBA</span></div>
  <div class="footer-time">
    <div class="time-line">Time : <span class="time-value">5pm - 7.30pm</span></div>
    <div class="time-note">(followed by dinner and case presentations.)</div>
  </div>
</div>
</body>
</html>
```